Velbrook Global Policy Document/Report Template for consistent document outputs

We need a policy document/report template that we can disseminate to staff so all produced documents look the same, and less formatting has to be done each time a policy or report is started.
VBG applies the power of biological science, physical science, and IT to solve the most challenging mission problems encompassing Forensics, Biometrics, Weapons Technical and Identity Intelligence, CBRNE, CWMD, and Public Health initiatives. Here is a list of requirements for the document:
• Cover page
o Include full logo
o Title
o Possibly a subtitle
o Version #
o Date
o We want a common look that all policy documents will follow, and it is easy to recognize
o Some color and a unique look and feel
• Header and Footer (2nd page on)
o Both header and footer must include this language: “Confidential and Proprietary - For Velbrook Global Internal Use Only,” so it appears at the top and bottom of the page
o The document title must be in either the header or footer
• Header (after first page)
o Include logo
• Footer (not counting title page)
o Must include date, and page X of Y
• 4 levels of headings, numbered 1, 1.1, 1.1.1, 1.1.1.1
• 4 levels of bullets with color/style
• Design for a callout box
• Design or a box containing a quote
• Two table designs
• Pages (other than the title page)
o Pages are primarily white
o Colors for accent and visual interest

Finally, our corporate font is Source Sans Pro.
The swirl pattern on our logo has no special meaning (but feel free to use it as a design element).

Font styles to use
Other font styles liked:
• Source Sans Pro

Requirements
Must have
• See description for more information: Cover page, header and footer, multiple heading levels, callout box, tables

```html
<!DOCTYPE html>
<html lang="en">
<head>
<meta charset="utf-8">
<title>Velbrook Global – Report Template Pages</title>
<link href="https://fonts.googleapis.com/css2?family=Source+Sans+3:ital,wght@0,400;0,600;0,700;0,900;1,600;1,700&display=swap" rel="stylesheet">
<style>
:root{
  --purple:#3d2a78;
  --crimson:#c4203c;
  --ink:#222;
  --body:#5a5a66;
  --grey-cell:#d9d9dc;
  --stage:#6a6a6a;
  --grad:linear-gradient(90deg,var(--purple),var(--crimson));
}
*{margin:0;padding:0;box-sizing:border-box}
html,body{width:1000px;height:1200px;overflow:hidden;background:var(--stage);font-family:"Source Sans 3","Source Sans Pro",sans-serif}
.sheet{position:relative;width:1000px;height:1200px}
.page{position:absolute;width:181px;height:233px;background:#fff;overflow:hidden;box-shadow:0 1px 3px rgba(0,0,0,.35)}
.b{position:absolute}
/* running header */
.hdr{position:absolute;left:0;top:6px;right:0;height:9px;border-bottom:.4px solid #e3dfe9}
.hdr-bar{position:absolute;left:0;top:0;width:57px;height:8px;background:var(--grad)}
.hdr-txt{position:absolute;left:60px;top:.5px;font-size:2.6px;line-height:3.2px;color:#777}
.hdr-txt b{display:block;color:var(--purple);font-weight:700}
.hdr-txt em{font-style:normal;color:var(--crimson);font-weight:700}
/* running footer */
.ftr{position:absolute;left:16px;right:0;top:213px;height:12px;border-bottom:.5px solid var(--purple)}
.ftr-logo{position:absolute;left:0;top:3px;font-size:5px;font-weight:700;color:var(--purple)}
.ftr-logo::before{content:"";display:inline-block;width:3.4px;height:3.4px;border-radius:50%;border:.6px solid var(--crimson);margin-right:1px;vertical-align:-.2px}
.ftr-txt{position:absolute;left:17px;top:2.6px;font-size:2.2px;line-height:2.8px;color:#777}
.ftr-txt em{font-style:normal;color:var(--crimson);font-weight:700}
.ftr-pg{position:absolute;right:40px;top:0;font-size:2.8px;color:#444}
.ftr-bar{position:absolute;right:0;bottom:-.5px;width:48px;height:3px;background:var(--grad)}
/* headings */
.h1{font-size:6px;font-weight:700;color:var(--purple)}
.h1 span{margin-right:5px}
.h2{font-size:3.6px;font-weight:700;color:var(--purple)}
.h2 span{margin-right:4px}
.h3{font-size:3.3px;font-weight:700;font-style:italic;color:var(--purple)}
.h4{font-size:2.8px;font-weight:700;font-style:italic;color:var(--crimson)}
.h4 span{margin-right:5px}
.tx{font-size:2.5px;line-height:3.55px;color:var(--body);text-align:justify}
.tx p+p{margin-top:2px}
.cap{font-size:2px;color:#999;font-style:italic}
.bul{font-size:2.5px;line-height:3.9px;color:var(--body);list-style:none}
.bul li::before{content:"";display:inline-block;width:1.2px;height:1.2px;border-radius:50%;background:var(--ink);margin-right:3px;vertical-align:.5px}
.photo{position:absolute}
.chart{position:absolute;border:.4px solid #ddd;background:#fff}
/* data tables */
.dtab{position:absolute;border-collapse:collapse}
.dtab td{border:.5px solid #fff;height:5.3px}
.dtab tr:first-child td{background:var(--purple)}
.dtab td:first-child{background:var(--purple)}
.dtab tr+tr td+td{background:var(--grey-cell)}
/* cover */
.cover-city{position:absolute;left:0;top:0;width:181px;height:205px;background:linear-gradient(180deg,#f4f4f7 0%,#eceef3 55%,#fff 100%)}
.cover-logo{position:absolute;right:14px;top:15px;font-size:9px;font-weight:700;color:var(--purple);line-height:9px}
.cover-logo::before{content:"";display:inline-block;width:6px;height:6px;border-radius:50%;border:1px solid var(--crimson);margin-right:2px;vertical-align:0}
.cover-title{position:absolute;left:57px;top:126px;font-size:13.5px;font-weight:900;color:#111;letter-spacing:-.1px}
.cover-sub{position:absolute;left:58px;top:143px;font-size:2.6px;color:var(--crimson);font-weight:600}
.cover-band{position:absolute;left:0;top:205px;width:181px;height:28px;background:var(--grad)}
.cover-meta{position:absolute;left:30px;top:210px;width:120px;border-collapse:collapse;color:#fff;font-size:2.6px;text-align:center}
.cover-meta th{font-weight:700;border-bottom:.4px solid rgba(255,255,255,.8);padding:.5px 0 1px}
.cover-meta td{border:.4px solid rgba(255,255,255,.8);padding:1px 0;color:#eee}
/* contents page */
.toc-band{position:absolute;left:0;top:0;width:181px;height:47px;background:linear-gradient(90deg,#3a2a72 0%,#4a2a74 45%,#8a2250 60%,#b3203f 68%)}
.toc-form{position:absolute;left:10px;top:4px;width:80px}
.toc-form div{height:8.4px;border-bottom:.4px solid rgba(255,255,255,.45);display:flex;align-items:center;font-size:2.4px;color:#e8e4f2}
.toc-form div span{width:24px;text-align:right;padding-right:3px;border-right:.4px solid rgba(255,255,255,.45);height:100%;display:flex;align-items:center;justify-content:flex-end}
.toc-title{position:absolute;left:21px;top:55px;font-size:5.6px;font-weight:700;color:var(--purple)}
.toc{position:absolute;left:21px;top:69px;width:129px;font-size:2.4px;color:#777}
.toc .r{display:flex;align-items:flex-end;height:4px}
.toc .r i{flex:1;border-bottom:.4px dotted #888;margin:0 .5px .6px}
.toc .m{color:var(--purple);font-weight:700;height:5.8px;margin-top:2.2px}
.toc .s{padding-left:5px}
.toc .t{padding-left:3px;font-size:1.9px;height:2.9px}
.toc .q{padding-left:7px;font-size:1.9px;height:2.9px}
/* quote + callout */
.quote{position:absolute;border-left:1px solid var(--crimson);padding-left:3px;font-size:2.5px;line-height:3.4px;color:var(--body)}
.quote.strong{font-size:3.6px;line-height:6.3px;font-weight:700;color:var(--purple)}
.callout{position:absolute;background:linear-gradient(135deg,var(--purple),#7a2a6a 60%,var(--crimson));color:#f2eef8;font-size:2.2px;line-height:3.1px;padding:4px 3px;text-align:justify}
.kt{font-size:2.7px;font-weight:700;color:var(--purple)}
</style>
</head>
<body>
<div class="sheet">

<!-- 1 cover -->
<section class="page" style="left:107px;top:102px">
  <div class="cover-city" role="img" aria-label="Faint pale city skyline backdrop"></div>
  <div class="cover-logo">VBG</div>
  <div class="cover-title">Project Report</div>
  <div class="cover-sub">Velbrook Global - applied science for every mission</div>
  <div class="cover-band"></div>
  <table class="cover-meta">
    <tr><th>Date</th><th>Location</th><th>Version</th></tr>
    <tr><td>[PROJECT DATE]</td><td>[PROJECT Location]</td><td>[Version]</td></tr>
  </table>
</section>

<!-- 2 contents -->
<section class="page" style="left:311px;top:102px">
  <div class="toc-band"></div>
  <div class="photo" role="img" aria-label="Glowing digital network head artwork" style="left:96px;top:0;width:85px;height:47px;background:linear-gradient(120deg,rgba(178,32,63,0) 0%,#1b3550 35%,#1f6b86 60%,#0d1a2e 100%)"></div>
  <div class="toc-form">
    <div><span>Project</span></div><div><span>Project No.</span></div><div><span>Document No.</span></div><div><span>Author</span></div><div><span>Date</span></div>
  </div>
  <div class="toc-title">Table of Contents</div>
  <div class="toc">
    <div class="r m">1&nbsp;&nbsp;&nbsp;Document History<i></i>3</div>
    <div class="r s">1.1&nbsp;&nbsp;&nbsp;Revision History<i></i>3</div>
    <div class="r s">1.2&nbsp;&nbsp;&nbsp;Revision History<i></i>3</div>
    <div class="r m">2&nbsp;&nbsp;&nbsp;Conclusion<i></i>4</div>
    <div class="r m">3&nbsp;&nbsp;&nbsp;Executive Summary<i></i>5</div>
    <div class="r s">3.1&nbsp;&nbsp;&nbsp;Project Overview<i></i>5</div>
    <div class="r s">3.2&nbsp;&nbsp;&nbsp;Key Achievements<i></i>5</div>
    <div class="r m">4&nbsp;&nbsp;&nbsp;Main Report<i></i>6</div>
    <div class="r s">4.1&nbsp;&nbsp;&nbsp;Project Objectives &amp; Scope<i></i>6</div>
    <div class="r s">4.2&nbsp;&nbsp;&nbsp;Components of the Project<i></i>7</div>
    <div class="r s">4.3&nbsp;&nbsp;&nbsp;Defining the Purpose<i></i>8</div>
    <div class="r s">4.4&nbsp;&nbsp;&nbsp;Project Phases and Timeline<i></i>2</div>
    <div class="r t">4.4.1&nbsp;&nbsp;Chronicle of Programs<i></i>2</div>
    <div class="r t">4.4.2&nbsp;&nbsp;ignimus estion<i></i>3</div>
    <div class="r q">4.4.2.1&nbsp;&nbsp;&nbsp;illabor sumquis<i></i>3</div>
    <div class="r q">4.4.2.2&nbsp;&nbsp;&nbsp;doloria bea<i></i>3</div>
    <div class="r q">4.4.2.3&nbsp;&nbsp;&nbsp;Poria cumquae pratur<i></i>4</div>
    <div class="r q">4.4.2.4&nbsp;&nbsp;&nbsp;Poria cumquae pratur sequi as<i></i>4</div>
    <div class="r q">4.4.2.5&nbsp;&nbsp;&nbsp;quaernam undi<i></i>4</div>
  </div>
</section>

<!-- 3 phases -->
<section class="page" style="left:513px;top:102px">
  <div class="hdr"><div class="hdr-bar"></div><div class="hdr-txt"><b>DOCUMENT TITLE</b><em>Confidential and Proprietary</em> - For Velbrook Global Internal Use Only.</div></div>
  <div class="b h2" style="left:21px;top:22px"><span>4.4</span>Project Phases and Timeline</div>
  <div class="b tx" style="left:21px;top:30px;width:139px">Vendi comnihit dunt accum hillectium exceaquiam este net dolum audam fugia sitatem. Ut quas dolorio bea ium quis a volores incipit assimag nimilig endeles tisque peritat et faceptiunt quas moloreatem nobis dentem qui blaut quo qui bea voluptatur, iuscid moluptatem. Xerore modi con re con rem ipiditibus, net electot aquisci alitiberum quiae dolecust imagni iditis secearum este plabore hendell ignimus estion re omnimin consero illabor sumquis.</div>
  <div class="b h3" style="left:32px;top:64px">4.4.1&nbsp;&nbsp;Chronicle of Programs</div>
  <svg class="chart" style="left:21px;top:72px" width="68" height="50" viewBox="0 0 68 50">
    <text x="34" y="6" font-size="2.8" fill="#666" text-anchor="middle">Series 1</text>
    <g font-size="1.6" fill="#888"><text x="2" y="14">Category 4</text><text x="2" y="19">Category 3</text><text x="2" y="24">Category 2</text><text x="2" y="29">Category 1</text></g>
    <rect x="15" y="11.5" width="40" height="1.4" fill="#c4203c"/><rect x="15" y="13" width="24" height="1.4" fill="#3d2a78"/>
    <rect x="15" y="16.5" width="33" height="1.4" fill="#c4203c"/><rect x="15" y="18" width="30" height="1.4" fill="#3d2a78"/>
    <rect x="15" y="21.5" width="20" height="1.4" fill="#c4203c"/><rect x="15" y="23" width="28" height="1.4" fill="#3d2a78"/>
    <rect x="15" y="26.5" width="36" height="1.4" fill="#c4203c"/><rect x="15" y="28" width="22" height="1.4" fill="#3d2a78"/>
    <g font-size="1.5" fill="#888"><text x="15" y="35">0</text><text x="25" y="35">1</text><text x="35" y="35">2</text><text x="45" y="35">3</text><text x="55" y="35">4</text></g>
    <g font-size="1.5" fill="#888"><text x="18" y="40">■ Category 1 ■ Category 2</text><text x="18" y="44">■ Category 3 ■ Category 4</text></g>
  </svg>
  <div class="b cap" style="left:21px;top:124px">Figure 2</div>
  <div class="b tx" style="left:94px;top:72px;width:66px">nimilig endeles tisque peritat et faceptiunt quas moloreatem nobis dentem qui blaut quo qui bea voluptatur, iuscid moluptatem. Xerore modi con re con rem ipiditibus, net electot aquisci alitiberum quiae dolecust moloreatem nobis dentem qui blaut quo qui bea voluptatur, iuscid moluptatem. Xerore modi con re con rem ipiditibus, net electot aquisci alitiberum quiae dolecust</div>
  <div class="b tx" style="left:21px;top:131px;width:66px">moloreatem nobis dentem qui blaut quo qui bea voluptatur, iuscid moluptatem. Xerore modi con re con rem ipiditibus, net electot aquisci alitiberum quiae dolecust doloria bea ium quis a volores incipit assimag nimilig endeles tisque peritat et faceptiunt quas moloreatem nobis dentem qui blaut quo qui bea voluptatur, iuscid moluptatem. Xerore modi con re con rem ipiditibus, net electot aquisci alitiberum quiae dolecust imagni iditis secearum este plabore hendell ignimus estion re omnimin consero illabor sumquis</div>
  <div class="b tx" style="left:94px;top:131px;width:66px">dolorio bea ium quis a volores incipit assimag nimilig endeles tisque peritat et faceptiunt quas moloreatem nobis dentem qui blaut quo qui bea voluptatur, iuscid moluptatem. Xerore modi con re con rem ipiditibus, net electot aquisci alitiberum quiae dolecust imagni iditis secearum este plabore hendell ignimus estion re omnimin consero illabor sumquis<br><br>ipiditibus, net electot aquisci alitiberum quiae dolecust imagni iditis secearum este plabore</div>
  <div class="ftr"><span class="ftr-logo">VBG</span><span class="ftr-txt"><em>Confidential and Proprietary</em><br>For Velbrook Global Internal Use Only.</span><span class="ftr-pg">Page | 2 of 17</span><div class="ftr-bar"></div></div>
</section>

<!-- 4 line chart -->
<section class="page" style="left:730px;top:102px">
  <div class="hdr"><div class="hdr-bar"></div><div class="hdr-txt"><b>DOCUMENT TITLE</b><em>Confidential and Proprietary</em> - For Velbrook Global Internal Use Only.</div></div>
  <div class="b h3" style="left:32px;top:22px">4.4.2&nbsp;&nbsp;ignimus estion</div>
  <svg class="chart" style="left:21px;top:29px" width="134" height="73" viewBox="0 0 134 73">
    <text x="67" y="6" font-size="3" fill="#666" text-anchor="middle">Sales</text>
    <g stroke="#e6e6e6" stroke-width=".3"><line x1="10" y1="11" x2="128" y2="11"/><line x1="10" y1="16.5" x2="128" y2="16.5"/><line x1="10" y1="22" x2="128" y2="22"/><line x1="10" y1="27.5" x2="128" y2="27.5"/><line x1="10" y1="33" x2="128" y2="33"/><line x1="10" y1="38.5" x2="128" y2="38.5"/><line x1="10" y1="44" x2="128" y2="44"/><line x1="10" y1="49.5" x2="128" y2="49.5"/><line x1="10" y1="55" x2="128" y2="55"/></g>
    <g font-size="1.6" fill="#888"><text x="5" y="12">9</text><text x="5" y="23">7</text><text x="5" y="34">5</text><text x="5" y="45">3</text><text x="5" y="56">1</text></g>
    <polyline points="22,16 54,42 86,52 118,53" fill="none" stroke="#3d2a78" stroke-width=".8"/>
    <g font-size="1.7" fill="#888" text-anchor="middle"><text x="22" y="62">1st Qtr</text><text x="54" y="62">2nd Qtr</text><text x="86" y="62">3rd Qtr</text><text x="118" y="62">4th Qtr</text></g>
    <g font-size="1.5" fill="#888"><text x="35" y="68">— 1st Qtr&nbsp;&nbsp;— 2nd Qtr&nbsp;&nbsp;— 3rd Qtr&nbsp;&nbsp;— 4th Qtr</text></g>
  </svg>
  <div class="b cap" style="left:21px;top:105px">Figure 3</div>
  <div class="b tx" style="left:21px;top:110px;width:139px">moloreatem nobis dentem qui blaut quo qui bea voluptatur, iuscid moluptatem. Xerore modi con re con rem ipiditibus, net electot aquisci alitiberum quiae dolecust doloria bea ium quis a volores incipit assimag nimilig endeles tisque peritat et faceptiunt quas moloreatem nobis dentem qui blaut quo qui bea voluptatur, iuscid moluptatem. Xerore modi con re con rem ipiditibus, net electot aquisci alitiberum quiae dolecust imagni iditis secearum este plabore hendell ignimus estion re omnimin consero</div>
  <div class="b h4" style="left:27px;top:151px"><span>4.4.2.1</span>illabor sumquis</div>
  <div class="b tx" style="left:21px;top:157px;width:139px">dolorio bea ium quis a volores incipit assimag nimilig endeles tisque peritat et faceptiunt quas moloreatem nobis dentem qui blaut quo qui bea voluptatur, iuscid moluptatem. Xerore modi con re con rem ipiditibus, net electot aquisci alitiberum quiae dolecust imagni iditis secearum este plabore hendell</div>
  <div class="b h4" style="left:27px;top:184px"><span>4.4.2.2</span>doloria bea</div>
  <div class="b tx" style="left:21px;top:190px;width:139px">ium quis a volores incipit assimag nimilig endeles tisque peritat et faceptiunt quas moloreatem nobis dentem qui blaut quo qui bea voluptatur, iuscid moluptatem. Xerore modi con re con rem ipiditibus,</div>
  <div class="ftr"><span class="ftr-logo">VBG</span><span class="ftr-txt"><em>Confidential and Proprietary</em><br>For Velbrook Global Internal Use Only.</span><span class="ftr-pg">Page | 3 of 17</span><div class="ftr-bar"></div></div>
</section>

<!-- 5 document history -->
<section class="page" style="left:110px;top:359px">
  <div class="hdr"><div class="hdr-bar"></div><div class="hdr-txt"><b>DOCUMENT TITLE</b><em>Confidential and Proprietary</em> - For Velbrook Global Internal Use Only.</div></div>
  <div class="b h1" style="left:21px;top:22px"><span>1</span>Document History</div>
  <div class="b h2" style="left:21px;top:42px"><span>1.1</span>Revision History</div>
  <div class="b tx" style="left:21px;top:49px">The document has been revised by:</div>
  <div class="b cap" style="left:21px;top:59px">Table 1</div>
  <table class="dtab" style="left:21px;top:65px;width:138px">
    <tr><td style="width:27px"></td><td></td><td></td><td></td><td></td></tr>
    <tr><td></td><td></td><td></td><td></td><td></td></tr>
    <tr><td></td><td></td><td></td><td></td><td></td></tr>
    <tr><td></td><td></td><td></td><td></td><td></td></tr>
    <tr><td></td><td></td><td></td><td></td><td></td></tr>
  </table>
  <div class="b h2" style="left:21px;top:106px"><span>1.2</span>Revision History</div>
  <div class="b tx" style="left:21px;top:113px">Please see the following documents for more information:</div>
  <div class="b cap" style="left:21px;top:123px">Table 2</div>
  <table class="dtab" style="left:21px;top:129px;width:138px">
    <tr><td style="width:27px"></td><td></td><td></td><td></td><td></td></tr>
    <tr><td></td><td></td><td></td><td></td><td></td></tr>
    <tr><td></td><td></td><td></td><td></td><td></td></tr>
    <tr><td></td><td></td><td></td><td></td><td></td></tr>
    <tr><td></td><td></td><td></td><td></td><td></td></tr>
  </table>
  <div class="ftr"><span class="ftr-logo">VBG</span><span class="ftr-txt"><em>Confidential and Proprietary</em><br>For Velbrook Global Internal Use Only.</span><span class="ftr-pg">Page | 3 of 17</span><div class="ftr-bar"></div></div>
</section>

<!-- 6 conclusion -->
<section class="page" style="left:312px;top:359px">
  <div class="hdr"><div class="hdr-bar"></div><div class="hdr-txt"><b>DOCUMENT TITLE</b><em>Confidential and Proprietary</em> - For Velbrook Global Internal Use Only.</div></div>
  <div class="b h1" style="left:21px;top:22px"><span>2</span>Conclusion</div>
  <div class="quote" style="left:15px;top:42px;width:47px">“vendi comnihit dunt accum hillectium exceaquiam este net dolum audam fugia sitatem. Ut quas dolorio bea ium quis a volores incipit assimag nimilig endeles tisque peritat et faceptiunt quas moloreatem nobis dentem qui blaut quo qui bea voluptatur, iuscid moluptatem. Xerore mod”</div>
  <div class="b kt" style="left:21px;top:133px">Key Takeaways</div>
  <ul class="b bul" style="left:23px;top:141px">
    <li>Et molupta tquodic te</li><li>evendel iducil eaquias</li><li>soluptamento quaerna</li><li>undi nonsequas dolo que</li>
  </ul>
  <div class="b tx" style="left:71px;top:41px;width:89px">
    <p>vel modis sit accus, offcte nturia net am inis nonse optatus doluptae dolorioam voluptatur, in reped ulparum atemperum et iam quam elictatur ad minvellab invenum eaquam elia aspicid illectiae venis accum ea comnit as ius as sturestintur si rehenecae cusa volore nobitatur sit adignim incient faccatur? Quid mil et es modios ipsus sam iusanto tem rehenih illuptam fugiatet idel ibus res voloribus volorem eniatem quid quam vendam, voluptatur, aut hilita dolene cumque</p>
    <p>vendi comnihit dunt accum hillectium exceaquiam este net dolum audam fugia sitatem. Ut quas dolorio bea ium quis a volores incipit assimag nimilig endeles tisque peritat et faceptiunt quas moloreatem nobis dentem qui blaut quo qui bea voluptatur, iuscid moluptatem. Xerore modi con re con rem ipiditibus, net electot aquisci alitiberum quiae dolecust imagni iditis secearum este plabore hendell ignimus estion re omnimin consero illabor sumquis dissus aut offici dolupid undicianis quo omnimos etur re poria cumquae pratur sequi as eicimus, oditiissit</p>
    <p>vendi comnihit dunt accum hillectium exceaquiam este net dolum audam fugia sitatem. Ut quas dolorio bea ium quis a volores incipit assimag nimilig endeles tisque peritat et faceptiunt quas moloreatem nobis dentem qui blaut quo qui bea voluptatur, iuscid moluptatem. Xerore modi con re con rem ipiditibus, net electot aquisci alitiberum quiae dolecust imagni iditis secearum este plabore hendell ignimus estion re omnimin consero illabor sumquis dissus aut .</p>
  </div>
  <div class="ftr"><span class="ftr-logo">VBG</span><span class="ftr-txt"><em>Confidential and Proprietary</em><br>For Velbrook Global Internal Use Only.</span><span class="ftr-pg">Page | 4 of 17</span><div class="ftr-bar"></div></div>
</section>

<!-- 7 sub-sections -->
<section class="page" style="left:512px;top:359px">
  <div class="hdr"><div class="hdr-bar"></div><div class="hdr-txt"><b>DOCUMENT TITLE</b><em>Confidential and Proprietary</em> - For Velbrook Global Internal Use Only.</div></div>
  <div class="b tx" style="left:21px;top:21px;width:139px">net electot aquisci alitiberum quiae dolecust imagni iditis secearum este plabore hendell ignimus estion re omnimin consero illabor sumquis</div>
  <div class="b h4" style="left:27px;top:35px"><span>4.4.2.3</span>Poria cumquae pratur</div>
  <div class="b tx" style="left:21px;top:41px;width:139px">sequi as eicimus, oditiissit aut officiae magnisi conse doluptatium estrum nonsed molent minti as alis asped utas nienis minimusape verum fuga. Et molupta tquodic te evendel iducil eaquias soluptamento quaernam undi nonsequas dolo que dolo et omnisci sita aces aces aliquiame eost occullo rererit acest, sin nobis excest, sequo volorendi incilis apersesseque venihicit aut aut esti sunt adit, que commolu ptatur autempos verumqu iandellam, sincillam vellupti optatur? Equatur maxim dolorem nusdanimin poria quaturendisi si anda qui odis vel modis sit accus, offcte nturia net am inis nonse</div>
  <div class="b h4" style="left:27px;top:82px"><span>4.4.2.4</span>Poria cumquae pratur sequi as</div>
  <div class="b tx" style="left:21px;top:88px;width:139px">eicimus, oditiissit aut officiae magnisi conse doluptatium estrum nonsed molent minti as alis asped utas nienis minimusape verum fuga. Et molupta tquodic te evendel iducil eaquias soluptamento quaernam undi nonsequas dolo que dolo et omnisci sita aces aces aliquiame eost occullo rererit acest, sin nobis excest, sequo volorendi incilis apersesseque venihicit aut aut esti sunt adit, que commolu ptatur autempos verumqu iandellam, sincillam vellupti optatur? Equatur maxim dolorem nusdanimin poria quaturendisi si anda qui odis vel modis sit accus, offcte nturia net am inis nonse</div>
  <div class="b h4" style="left:27px;top:129px"><span>4.4.2.5</span>quaernam undi</div>
  <div class="b tx" style="left:21px;top:135px;width:139px">nonsequas dolo que dolo et omnisci sita aces aces aliquiame eost occullo rererit acest, sin nobis excest, sequo volorendi incilis apersesseque venihicit aut aut esti sunt adit, que commolu ptatur autempos verumqu iandellam, sincillam vellupti optatur? Equatur maxim dolorem nusdanimin poria quaturendisi si anda qui odis vel modis sit accus, offcte nturia net am inis nonse</div>
  <div class="b h4" style="left:27px;top:162px"><span>4.4.2.6</span>quaernam</div>
  <div class="b tx" style="left:21px;top:168px;width:139px">undi nonsequas dolo que dolo et omnisci sita aces aces aliquiame eost occullo rererit acest, sin nobis excest, sequo volorendi incilis apersesseque venihicit aut aut esti sunt adit, que commolu ptatur autempos verumqu iandellam, sincillam vellupti optatur? Equatur maxim dolorem nusdanimin poria quaturendisi si anda qui odis vel modis sit accus, offcte nturia net am inis nonse</div>
  <div class="ftr"><span class="ftr-logo">VBG</span><span class="ftr-txt"><em>Confidential and Proprietary</em><br>For Velbrook Global Internal Use Only.</span><span class="ftr-pg">Page | 4 of 17</span><div class="ftr-bar"></div></div>
</section>

<!-- 8 site overview -->
<section class="page" style="left:728px;top:359px">
  <div class="hdr"><div class="hdr-bar"></div><div class="hdr-txt"><b>DOCUMENT TITLE</b><em>Confidential and Proprietary</em> - For Velbrook Global Internal Use Only.</div></div>
  <div class="b h2" style="left:21px;top:21px"><span>4.5</span>Geographical Location and Site Overview</div>
  <div class="photo" role="img" aria-label="City skyline at sunset" style="left:21px;top:34px;width:135px;height:59px;background:linear-gradient(180deg,#4a5f8a 0%,#c98a6a 40%,#7a5a66 65%,#3a3346 100%)"></div>
  <div class="callout" style="left:31px;top:60px;width:51px;height:67px">dolorio bea ium quis a volores incipit assimag nimilig endeles tisque peritat et faceptiunt quas moloreatem nobis dentem qui blaut quo qui bea voluptatur, iuscid moluptatem. Xerore modi con re con rem ipiditibus, net electot aquisci alitiberum quiae dolecust imagni iditis secearum este plabore hendell ignimus estion re omnimin consero illabor sumquis</div>
  <div class="b kt" style="left:100px;top:99px">Key Achievements</div>
  <ul class="b bul" style="left:100px;top:107px">
    <li>aquisci alitiberum quiae dolecust</li><li>imagni iditis secearum este plabore</li><li>aquisci alitiberum quiae dolecust</li><li>aquisci alitiberum quiae dolecust</li>
  </ul>
  <div class="b tx" style="left:21px;top:142px;width:139px">
    <p>moloreatem nobis dentem qui blaut quo qui bea voluptatur, iuscid moluptatem. Xerore modi con re con rem ipiditibus, net electot aquisci alitiberum quiae dolecust doloria bea ium quis a volores incipit assimag nimilig endeles tisque peritat et faceptiunt quas moloreatem nobis dentem qui blaut quo qui bea voluptatur, iuscid moluptatem.</p>
    <p>Xerore modi con re con rem ipiditibus, net electot aquisci alitiberum quiae dolecust imagni iditis secearum este plabore hendell ignimus estion re omnimin consero illabor sumquis moloreatem nobis dentem qui blaut quo qui bea voluptatur, iuscid moluptatem. Xerore modi con re con rem ipiditibus, net electot aquisci alitiberum quiae dolecust doloria bea ium quis a volores incipit assimag nimilig endeles tisque peritat et faceptiunt quas moloreatem nobis dentem qui blaut quo qui bea voluptatur, iuscid moluptatem.</p>
  </div>
  <div class="ftr"><span class="ftr-logo">VBG</span><span class="ftr-txt"><em>Confidential and Proprietary</em><br>For Velbrook Global Internal Use Only.</span><span class="ftr-pg">Page | 5 of 17</span><div class="ftr-bar"></div></div>
</section>

<!-- 9 executive summary -->
<section class="page" style="left:110px;top:614px">
  <div class="hdr"><div class="hdr-bar"></div><div class="hdr-txt"><b>DOCUMENT TITLE</b><em>Confidential and Proprietary</em> - For Velbrook Global Internal Use Only.</div></div>
  <div class="b h1" style="left:21px;top:22px"><span>3</span>Executive Summary</div>
  <div class="photo" role="img" aria-label="Glass skyscrapers against blue sky" style="left:124px;top:22px;width:57px;height:99px;background:linear-gradient(160deg,#bcd3ea 0%,#5b7fa6 45%,#233a5a 100%)"></div>
  <div class="b tx" style="left:21px;top:40px;width:89px">vendi comnihit dunt accum hillectium exceaquiam este net dolum audam fugia sitatem. Ut quas dolorio bea ium quis a volores incipit assimag nimilig endeles tisque peritat et faceptiunt quas moloreatem nobis dentem qui blaut quo qui bea voluptatur, iuscid moluptatem. Xerore modi con re con rem ipiditibus, net electot aquisci alitiberum quiae dolecust imagni iditis secearum este plabore hendell ignimus estion</div>
  <div class="b h2" style="left:21px;top:81px"><span>3.1</span>Project Overview</div>
  <div class="b cap" style="left:21px;top:91px">Table 3</div>
  <table class="dtab" style="left:21px;top:96px;width:89px">
    <tr><td style="width:29px"></td><td></td></tr>
    <tr><td></td><td></td></tr><tr><td></td><td></td></tr><tr><td></td><td></td></tr><tr><td></td><td></td></tr>
  </table>
  <div class="b h2" style="left:21px;top:136px"><span>3.2</span>Key Achievments</div>
  <div class="b tx" style="left:21px;top:144px;width:139px">Vendi comnihit dunt accum hillectium exceaquiam este net dolum audam fugia sitatem. Ut quas dolorio bea ium quis a volores incipit assimag nimilig endeles tisque peritat et faceptiunt quas moloreatem nobis dentem qui blaut quo qui bea voluptatur, iuscid moluptatem. Xerore modi con re con rem ipiditibus, net electot aquisci alitiberum quiae dolecust imagni iditis secearum este plabore hendell ignimus estion re omnimin consero illabor sumquis dissus aut offici dolupid undicianis quo omnimos etur re</div>
  <ul class="b bul" style="left:27px;top:175px;width:133px;line-height:3.5px;text-align:justify">
    <li>Poria cumquae pratur sequi as eicimus, oditiissit aut officiae magnisi conse doluptatium estrum nonsed molent minti as alis asped utas nienis minimusape verum fuga. Et molupta tquodic te evendel iducil eaquias soluptamento quaernam undi nonsequas dolo que dolo et omnisci sita aces aces aliquiame eost occullo rererit acest, sin nobis excest, sequo volorendi incilis apersesseque venihicit aut aut esti sunt adit, que commolu ptatur autempos verumqu iandellam, sincillam vellupti optatur? Equatur maxim dolorem nusdanimin poria quaturendisi si anda qui odis vel modis sit accus, offcte nturia net am inis nonse</li>
  </ul>
  <div class="ftr"><span class="ftr-logo">VBG</span><span class="ftr-txt"><em>Confidential and Proprietary</em><br>For Velbrook Global Internal Use Only.</span><span class="ftr-pg">Page | 5 of 17</span><div class="ftr-bar"></div></div>
</section>

<!-- 10 main report -->
<section class="page" style="left:312px;top:614px">
  <div class="hdr"><div class="hdr-bar"></div><div class="hdr-txt"><b>DOCUMENT TITLE</b><em>Confidential and Proprietary</em> - For Velbrook Global Internal Use Only.</div></div>
  <div class="b h1" style="left:21px;top:22px"><span>4</span>Main Report</div>
  <div class="photo" role="img" aria-label="Upward view of glass office towers" style="left:0;top:40px;width:181px;height:72px;background:radial-gradient(ellipse at 50% 45%,#dfe8f4 0%,#8da6c8 30%,#2e3f66 70%,#18213d 100%)"></div>
  <div class="b h2" style="left:21px;top:125px"><span>4.1</span>Project Objectives &amp; Scope</div>
  <div class="b tx" style="left:21px;top:134px;width:66px">
    <p>Vendi comnihit dunt accum hillectium exceaquiam este net dolum audam fugia sitatem. Ut quas dolorio bea ium quis a volores incipit assimag nimilig endeles tisque peritat et faceptiunt quas moloreatem nobis dentem qui blaut quo qui bea voluptatur, iuscid moluptatem. Xerore modi con re con rem ipiditibus,</p>
    <p>Net electot aquisci alitiberum quiae dolecust imagni iditis secearum este plabore hendell ignimus estion re omnimin consero illabor sumquis dissus aut offici dolupid undicianis quo omnimos etur re poria cumquae pratur sequi as</p>
  </div>
  <div class="b tx" style="left:94px;top:134px;width:66px">
    <p>eicimus, oditiissit aut officiae magnisi conse doluptatium estrum nonsed molent minti as</p>
    <p>Alis asped utas nienis minimusape verum fuga. Et molupta tquodic te evendel iducil eaquias soluptamento quaernam undi nonsequas dolo que dolo et omnisci sita aces aces aliquiame eost occullo rererit acest, sin nobis excest, sequo volorendi incilis apersesseque venihicit aut aut esti sunt adit, que commolu ptatur autempos verumqu iandellam, sincillam vellupti optatur? Equatur maxim dolorem nusdanimin poria quaturendisi si anda qui odis vel modis sit accus</p>
  </div>
  <div class="ftr"><span class="ftr-logo">VBG</span><span class="ftr-txt"><em>Confidential and Proprietary</em><br>For Velbrook Global Internal Use Only.</span><span class="ftr-pg">Page | 6 of 17</span><div class="ftr-bar"></div></div>
</section>

<!-- 11 location map -->
<section class="page" style="left:511px;top:619px">
  <div class="hdr"><div class="hdr-bar"></div><div class="hdr-txt"><b>DOCUMENT TITLE</b><em>Confidential and Proprietary</em> - For Velbrook Global Internal Use Only.</div></div>
  <div class="b h3" style="left:32px;top:22px">4.5.1&nbsp;&nbsp;Location Map</div>
  <div class="photo" role="img" aria-label="Dotted world map in colour on dark background" style="left:21px;top:29px;width:141px;height:58px;background:radial-gradient(ellipse at 50% 50%,#3c3150 0%,#242230 55%,#16161c 100%)"></div>
  <div class="b tx" style="left:21px;top:96px;width:141px">moloreatem nobis dentem qui blaut quo qui bea voluptatur, iuscid moluptatem. Xerore modi con re con rem ipiditibus, net electot aquisci alitiberum quiae dolecust doloria bea ium quis a volores incipit assimag nimilig endeles tisque peritat et faceptiunt quas moloreatem nobis dentem qui blaut quo qui bea voluptatur, iuscid moluptatem. moloreatem nobis dentem qui blaut quo qui bea voluptatur, iuscid moluptatem. Xerore modi con re con rem ipiditibus,</div>
  <svg class="chart" style="left:21px;top:131px" width="141" height="66" viewBox="0 0 141 66">
    <defs><linearGradient id="barA" x1="0" y1="0" x2="0" y2="1"><stop offset="0" stop-color="#c4203c"/><stop offset="1" stop-color="#3d2a78"/></linearGradient></defs>
    <text x="70" y="6" font-size="2.8" fill="#666" text-anchor="middle">Series 1</text>
    <g stroke="#ececec" stroke-width=".3"><line x1="8" y1="12" x2="136" y2="12"/><line x1="8" y1="22" x2="136" y2="22"/><line x1="8" y1="32" x2="136" y2="32"/><line x1="8" y1="42" x2="136" y2="42"/><line x1="8" y1="52" x2="136" y2="52"/></g>
    <g font-size="1.5" fill="#888"><text x="3" y="13">5</text><text x="3" y="23">4</text><text x="3" y="33">3</text><text x="3" y="43">2</text><text x="3" y="53">0</text></g>
    <rect x="20" y="18" width="12" height="34" fill="url(#barA)"/><rect x="52" y="32" width="12" height="20" fill="url(#barA)"/><rect x="84" y="24" width="12" height="28" fill="url(#barA)"/><rect x="116" y="17" width="12" height="35" fill="url(#barA)"/>
    <g font-size="1.5" fill="#888" text-anchor="middle"><text x="26" y="56">Category 1</text><text x="58" y="56">Category 2</text><text x="90" y="56">Category 3</text><text x="122" y="56">Category 4</text></g>
    <text x="70" y="61" font-size="1.4" fill="#888" text-anchor="middle">■ Category 1 ■ Category 2 ■ Category 3 ■ Category 4</text>
  </svg>
  <div class="b cap" style="left:21px;top:199px">Figure 4</div>
  <div class="ftr"><span class="ftr-logo">VBG</span><span class="ftr-txt"><em>Confidential and Proprietary</em><br>For Velbrook Global Internal Use Only.</span><span class="ftr-pg">Page | 6 of 17</span><div class="ftr-bar"></div></div>
</section>

<!-- 12 engineering -->
<section class="page" style="left:730px;top:619px">
  <div class="hdr"><div class="hdr-bar"></div><div class="hdr-txt"><b>DOCUMENT TITLE</b><em>Confidential and Proprietary</em> - For Velbrook Global Internal Use Only.</div></div>
  <div class="b h2" style="left:21px;top:30px"><span>4.6</span>Engineering Approaches</div>
  <div class="b tx" style="left:21px;top:37px;width:141px">Xerore modi con re con rem ipiditibus, net electot aquisci alitiberum quiae dolecust imagni iditis secearum este plabore hendell ignimus estion re omnimin consero illabor sumquis moloreatem nobis dentem qui blaut quo qui bea voluptatur, iuscid moluptatem. Xerore modi con re con rem ipiditibus, net electot aquisci alitiberum quiae dolecust doloria bea ium quis a volores incipit assimag nimilig endeles tisque peritat et faceptiunt quas moloreatem nobis dentem qui blaut quo qui bea voluptatur, iuscid moluptatem.</div>
  <div class="photo" role="img" aria-label="Laboratory flasks with glowing liquids" style="left:21px;top:69px;width:141px;height:36px;background:linear-gradient(90deg,#1a3a6a 0%,#2c5a90 35%,#c86a4a 55%,#3a4a8a 75%,#1a2a5a 100%)"></div>
  <div class="quote strong" style="left:20px;top:133px;width:50px">“Xerore modi con re con rem ipiditibus, net electot aquisci alitiberum quiae dolecust imagni iditis secearum este plabore hendell ignimus estion re ”</div>
  <div class="b tx" style="left:73px;top:133px;width:89px">
    <p>moloreatem nobis dentem qui blaut quo qui bea voluptatur, iuscid moluptatem. Xerore modi con re con rem ipiditibus, net electot aquisci alitiberum quiae dolecust doloria bea ium quis a volores incipit assimag nimilig endeles tisque peritat et faceptiunt quas moloreatem nobis dentem qui blaut quo qui bea voluptatur,</p>
    <p>re omnimin consero illabor sumquis moloreatem nobis dentem qui blaut quo qui bea voluptatur, iuscid moluptatem. Xerore modi con re con rem ipiditibus, net electot aquisci alitiberum quiae dolecust doloria bea ium quis a volores incipit assimag nimilig</p>
  </div>
  <div class="ftr"><span class="ftr-logo">VBG</span><span class="ftr-txt"><em>Confidential and Proprietary</em><br>For Velbrook Global Internal Use Only.</span><span class="ftr-pg">Page | 7 of 17</span><div class="ftr-bar"></div></div>
</section>

<!-- 13 components -->
<section class="page" style="left:110px;top:873px">
  <div class="hdr"><div class="hdr-bar"></div><div class="hdr-txt"><b>DOCUMENT TITLE</b><em>Confidential and Proprietary</em> - For Velbrook Global Internal Use Only.</div></div>
  <div class="b h2" style="left:21px;top:22px"><span>4.2</span>Components of the Project</div>
  <div class="b tx" style="left:21px;top:30px;width:139px">Vendi comnihit dunt accum hillectium exceaquiam este net dolum audam fugia sitatem. Ut quas dolorio bea ium quis a volores incipit assimag nimilig endeles tisque peritat et faceptiunt quas moloreatem nobis <span style="color:var(--crimson)">dentem</span> qui blaut quo qui bea voluptatur, iuscid moluptatem. Xerore modi con re con rem ipiditibus,</div>
  <svg class="chart" style="left:21px;top:56px" width="139" height="68" viewBox="0 0 139 68">
    <defs><linearGradient id="barB" x1="0" y1="0" x2="0" y2="1"><stop offset="0" stop-color="#c4203c"/><stop offset="1" stop-color="#3d2a78"/></linearGradient></defs>
    <text x="69" y="6" font-size="2.8" fill="#666" text-anchor="middle">Series 1</text>
    <g stroke="#ececec" stroke-width=".3"><line x1="8" y1="12" x2="134" y2="12"/><line x1="8" y1="22" x2="134" y2="22"/><line x1="8" y1="32" x2="134" y2="32"/><line x1="8" y1="42" x2="134" y2="42"/><line x1="8" y1="54" x2="134" y2="54"/></g>
    <g font-size="1.5" fill="#888"><text x="3" y="13">5</text><text x="3" y="23">4</text><text x="3" y="33">3</text><text x="3" y="43">2</text><text x="3" y="55">0</text></g>
    <rect x="19" y="18" width="12" height="36" fill="url(#barB)"/><rect x="51" y="34" width="12" height="20" fill="url(#barB)"/><rect x="83" y="26" width="12" height="28" fill="url(#barB)"/><rect x="115" y="17" width="12" height="37" fill="url(#barB)"/>
    <g font-size="1.5" fill="#888" text-anchor="middle"><text x="25" y="58">Category 1</text><text x="57" y="58">Category 2</text><text x="89" y="58">Category 3</text><text x="121" y="58">Category 4</text></g>
    <text x="69" y="63" font-size="1.4" fill="#888" text-anchor="middle">■ Category 1 ■ Category 2 ■ Category 3 ■ Category 4</text>
  </svg>
  <div class="b cap" style="left:21px;top:126px">Figure 1</div>
  <div class="b tx" style="left:21px;top:132px;width:66px">
    <p>Vendi comnihit dunt accum hillectium exceaquiam este net dolum audam fugia sitatem. Ut quas dolorio bea ium quis a volores incipit assimag nimilig endeles tisque peritat et faceptiunt quas moloreatem nobis dentem qui blaut quo qui bea voluptatur, iuscid moluptatem. Xerore modi con re con rem ipiditibus,</p>
    <p>Vendi comnihit dunt accum hillectium exceaquiam este net dolum audam fugia sitatem. Ut quas dolorio bea ium quis a volores incipit assimag nimilig endeles tisque peritat et faceptiunt quas moloreatem nobis dentem qui</p>
  </div>
  <div class="b tx" style="left:94px;top:132px;width:66px">
    <p>blaut quo qui bea voluptatur, iuscid moluptatem. Xerore modi con re con rem ipiditibus,</p>
    <p>Vendi comnihit dunt accum hillectium exceaquiam este net dolum audam fugia sitatem. Ut quas dolorio bea ium quis a volores incipit assimag nimilig endeles tisque peritat et faceptiunt quas moloreatem nobis dentem qui blaut quo qui bea voluptatur, iuscid moluptatem. Xerore modi con re con rem ipiditibus,</p>
  </div>
  <div class="ftr"><span class="ftr-logo">VBG</span><span class="ftr-txt"><em>Confidential and Proprietary</em><br>For Velbrook Global Internal Use Only.</span><span class="ftr-pg">Page | 7 of 17</span><div class="ftr-bar"></div></div>
</section>

<!-- 14 purpose -->
<section class="page" style="left:316px;top:873px">
  <div class="hdr"><div class="hdr-bar"></div><div class="hdr-txt"><b>DOCUMENT TITLE</b><em>Confidential and Proprietary</em> - For Velbrook Global Internal Use Only.</div></div>
  <div class="b h2" style="left:21px;top:22px"><span>4.3</span>Defining the Purpose</div>
  <div class="photo" role="img" aria-label="Tall glass tower seen from below" style="left:21px;top:31px;width:67px;height:117px;background:linear-gradient(160deg,#cfe0f0 0%,#6f93bb 40%,#2c4a72 100%)"></div>
  <div class="b tx" style="left:93px;top:31px;width:67px;line-height:3.45px">
    <p>Blaut quo qui bea voluptatur, iuscid moluptatem. Xerore modi con re con rem ipiditibus, net electot aquisci alitiberum quiae dolecust imagni iditis secearum este plabore hendell ignimus estion re omnimin consero illabor sumquis dissus aut offici dolupid undicianis quo omnimos etur re poria cumquae pratur sequi as eicimus, oditiissit aut officiae magnisi conse doluptatium estrum nonsed molent minti as alis asped utas nienis minimusape verum fuga. Et molupta tquodic te evendel iducil eaquias soluptamento.</p>
    <p>Xerore modi con re con rem ipiditibus, net electot aquisci alitiberum quiae dolecust imagni iditis secearum este plabore hendell ignimus estion re omnimin consero illabor sumquis dissus aut offici dolupid undicianis quo omnimos etur re poria cumquae pratur sequi as eicimus, oditiissit aut officiae magnisi conse doluptatium estrum nonsed molent minti as alis asped utas nienis minimusape verum fuga. Et molupta tquodic te evendel iducil eaquias soluptamento.</p>
  </div>
  <div class="photo" role="img" aria-label="Office towers against blue sky" style="left:21px;top:152px;width:139px;height:60px;background:linear-gradient(180deg,#e6eef7 0%,#8fb0d4 35%,#3b5d8a 75%,#223a5e 100%)"></div>
  <div class="ftr"><span class="ftr-logo">VBG</span><span class="ftr-txt"><em>Confidential and Proprietary</em><br>For Velbrook Global Internal Use Only.</span><span class="ftr-pg">Page | 8 of 17</span><div class="ftr-bar"></div></div>
</section>

<!-- 15 references -->
<section class="page" style="left:513px;top:873px">
  <div class="hdr"><div class="hdr-bar"></div><div class="hdr-txt"><b>DOCUMENT TITLE</b><em>Confidential and Proprietary</em> - For Velbrook Global Internal Use Only.</div></div>
  <div class="b h1" style="left:21px;top:23px"><span>5</span>References</div>
  <div class="ftr"><span class="ftr-logo">VBG</span><span class="ftr-txt"><em>Confidential and Proprietary</em><br>For Velbrook Global Internal Use Only.</span><span class="ftr-pg">Page | 8 of 17</span><div class="ftr-bar"></div></div>
</section>

<!-- 16 appendices -->
<section class="page" style="left:732px;top:873px">
  <div class="hdr"><div class="hdr-bar"></div><div class="hdr-txt"><b>DOCUMENT TITLE</b><em>Confidential and Proprietary</em> - For Velbrook Global Internal Use Only.</div></div>
  <div class="b h1" style="left:21px;top:23px"><span>6</span>Appendices</div>
  <div class="b h2" style="left:21px;top:42px"><span>6.1</span>Appendices 1</div>
  <div class="b h2" style="left:21px;top:60px"><span>6.2</span>Appendices 2</div>
  <div class="ftr"><span class="ftr-logo">VBG</span><span class="ftr-txt"><em>Confidential and Proprietary</em><br>For Velbrook Global Internal Use Only.</span><span class="ftr-pg">Page | 9 of 17</span><div class="ftr-bar"></div></div>
</section>

</div>
</body>
</html>
```